Energy Management - layout ideas in Photoshop + $20 participation to 2nd & 3rd place

Dear Designers

• I am looking for an Graphic designer with web experience
• No Html or CSS coding will be required

$20 participation payments to second & third place designs !

This project is for a design theme we can use for our new web site @

http://www.kestrelwattgrid.co.uk/

Basically we like the homepage designs & "Providing the Results" slogan but I'm not quite happy using a template and require slight changes to make it look more bespoke & original .

I only require illustrations if you can come up with the layout as Photoshop, Vector, power point or similar formats we can use them when coding the site .
Inspiration & Similar web sites

http://www.pravolent.com/
http://www.dorvakt.com/
http://www.trasquilpower.com/
http://www.velmora-systems.com/
http://www.qz7gaugeportal.co.uk/
http://www.amber-crest.com/energy/
http://www.pivarenergy.com/solutions/overview
http://www.qtbxl.com/open-system-solutions/

Our other business http://www.daltrygauges.com/remote-meter-reading.html

we have many domains on our dedicated server and will require future help with designs & have more work for the right designer's

here are some examples of clients using our hosted service listed below

http://www.bramvolt-monitor.co.uk/

http://www.tindaleco-monitor.co.uk/

http://www.qnbe-monitor.co.uk/

http://www.orvalcore-monitor.co.uk/

http://www.zep-energy.com/

Reason: We have extended the design deadline due to lack of submissions

Reason: We have been unable to give this project our full attention until now Apologies Derek

Target Market(s)

People / Business's who are interested in very advanced Energy related products , saving money and reducing carbon emissions

Industry/Entity Type

Business

Requirements
Must have
• - Clean-professional look

"Providing the Results" slogan

Modern theme based around technology & wireless networking

must be based around the http://www.kestrelwattgrid.co.uk/ theme concept
Nice to have
• Would be nice to point out our Carbon Neutral web site and hosted services

```html
<!DOCTYPE html>
<html lang="en">
<head>
<meta charset="utf-8">
<title>KestrelWattGrid – Home</title>
<link rel="stylesheet" href="https://fonts.googleapis.com/css2?family=Signika:wght@400;600&display=swap">
<style>
  :root {
    --navy: #173560;
    --navy-deep: #122b50;
    --nav-text: #c9d3e0;
    --nav-rule: #7f93b0;
    --white: #ffffff;
    --sky-light: #9fb0c6;
    --sky-mid: #7f93b0;
    --sky-dark: #5a7093;
    --silver-dark: #b3c0cf;
    --silver-light: #eef2f6;
    --body-text: #141a24;
    --leaf-light: #7ed957;
    --leaf-dark: #1f9a3c;
  }
  * { margin: 0; padding: 0; box-sizing: border-box; }
  html, body { width: 1200px; height: 900px; overflow: hidden; }
  body { font-family: "Signika", sans-serif; background: var(--silver-light); }

  .page {
    position: relative;
    width: 1200px;
    height: 900px;
    overflow: hidden;
    background: linear-gradient(115deg, var(--silver-dark) 0%, #c8d2dd 38%, var(--silver-light) 50%, #c5cfdb 62%, var(--silver-dark) 100%);
  }

  .masthead {
    position: absolute;
    left: 0; top: 0;
    width: 1200px; height: 412px;
    background: radial-gradient(ellipse at 20% 10%, #1e4272 0%, var(--navy) 55%, var(--navy-deep) 100%);
  }
  .masthead-base {
    position: absolute;
    left: 0; top: 404px;
    width: 1200px; height: 9px;
    background: var(--navy-deep);
  }

  .brand {
    position: absolute;
    left: 101px; top: 100px;
    display: flex;
    align-items: center;
    gap: 12px;
    color: var(--white);
    font-weight: 600;
  }
  .brand-name { font-size: 44px; line-height: 1; letter-spacing: 1px; }
  .brand-tagline { font-size: 11px; letter-spacing: 0.5px; margin-top: 4px; }
  .brand-dot {
    width: 22px; height: 22px;
    border-radius: 50%;
    background: var(--white);
  }

  .main-nav {
    position: absolute;
    left: 573px; top: 58px;
    width: 591px;
    display: flex;
    justify-content: space-between;
    border-bottom: 1px solid var(--nav-rule);
    padding-bottom: 8px;
  }
  .main-nav a {
    position: relative;
    color: var(--nav-text);
    text-decoration: none;
    font-size: 19px;
    letter-spacing: 1px;
    text-transform: uppercase;
  }
  .main-nav a.is-current::after {
    content: "";
    position: absolute;
    left: 0; right: 0; bottom: -11px;
    height: 4px;
    background: var(--nav-text);
  }

  .skyline {
    position: absolute;
    left: 0; top: 205px;
    width: 1200px; height: 199px;
    background: linear-gradient(180deg, var(--sky-light) 0%, var(--sky-mid) 55%, var(--sky-dark) 100%);
  }

  .emblem {
    position: absolute;
    left: 493px; top: 300px;
    width: 216px; height: 216px;
    border-radius: 50%;
    background: var(--navy);
    box-shadow: 0 6px 14px rgba(10, 25, 50, 0.45);
    display: flex;
    align-items: center;
    justify-content: center;
  }
  .emblem-art {
    width: 116px; height: 144px;
    border-radius: 46% 46% 40% 40%;
    background: linear-gradient(180deg, var(--leaf-light), var(--leaf-dark));
  }

  .intro {
    position: absolute;
    left: 88px; top: 574px;
    width: 1041px;
    color: var(--body-text);
    font-size: 17px;
    letter-spacing: 0.55px;
    line-height: 18.8px;
    text-align: justify;
    hyphens: auto;
  }
</style>
</head>
<body>
<div class="page">
  <header class="masthead">
    <div class="brand">
      <div>
        <div class="brand-name">KWG</div>
        <div class="brand-tagline">KestrelWattGrid</div>
      </div>
      <span class="brand-dot"></span>
    </div>
    <nav class="main-nav">
      <a href="#" class="is-current">Home</a>
      <a href="#">Solution</a>
      <a href="#">Production</a>
      <a href="#">Case Studies</a>
      <a href="#">Contact Us</a>
    </nav>
    <div class="skyline" role="img" aria-label="City skyline of glass office towers"></div>
  </header>
  <div class="masthead-base"></div>

  <div class="emblem">
    <div class="emblem-art" role="img" aria-label="Pair of green footprints representing carbon footprint"></div>
  </div>

  <main class="intro">
    <p>Lorem ipsum dolor sit amet, consectetur adipiscing elit. Proin porttitor odio eleifend ante luctus mattis. Nullam adipiscing ante vel dapibus venenatis. Pellentesque metus neque, aliquam vehicula justo at, venenatis sollicitudin erat. Maecenas blandit semper tortor quis vestibulum. Donec condimentum at odio eget egestas. Duis ut mollis est, eget aliquam nisi. Maecenas pulvinar sem non auctor elementum. Sed a urna mi. Nunc id commodo nunc.</p>
    <p>Vestibulum ut elit convallis, luctus massa sed, adipiscing diam. Suspendisse tristique convallis dui, id varius tellus commodo ac. Quisque quis ornare leo, vitae dictum libero. Phasellus faucibus nulla in lacus luctus, ac scelerisque est sagittis. Integer consequat justo varius cursus congue. Aenean pharetra mauris consequat elementum dignissim. Nam tempus consequat risus, vitae pretium metus suscipit euismod. Aliquam feugiat placerat risus, in sagittis urna lacinia ut. Mauris tristique quam ut augue sagittis, non feugiat nibh egestas. Proin eros lacus, bibendum nec ullamcorper vitae, semper rutrum dolor. Ut iaculis ullamcorper mi, varius eleifend ligula facilisis id. Quisque scelerisque enim a leo congue, id tempor elit porta. Vivamus sit amet rhoncus tortor, eu sollicitudin turpis. Proin id tortor et tellus eleifend dictum ultrices vitae libero. Aliquam erat volutpat.</p>
  </main>
</div>
</body>
</html>
```